Commercial Swimming Pool - Design-Build Contractor Website Design

I need a new website that will feature our newly developed logo and trade name as well as provide a fully updated site experience. We are not a residential builder - we strictly design and install high-end commercial pools. I need the website to highlight our portfolio and communicate the various types of projects in which we specialize. I want the effect of the site to reflect the high-end nature of our services - projects like the 57th floor spa at the Delmar Brightwater, the aquatic therapy portion of the Delmar Falcons training facility, a 5om indoor competition pool for the prestigious Thornwick Academy, the indoor water park at The Calloway Lodge or the recent country club renovation projects we've completed in our region (to name a few examples).

```html
<!DOCTYPE html>
<html lang="en">
<head>
<meta charset="utf-8">
<title>Marlow Aquatics — Commercial Pool Design-Build</title>
<link href="https://fonts.googleapis.com/css2?family=Jost:ital,wght@0,300;0,400;0,500;0,600;0,700;1,500;1,600&display=swap" rel="stylesheet">
<style>
:root{
  --blue-bright:#1b9be9;
  --blue-deep:#1463c6;
  --sky:#46b6e6;
  --sky-soft:#e3f4fc;
  --pale:#eaf6fd;
  --navy:#18265a;
  --ink:#1b1f2a;
  --grey:#6b7280;
  --white:#ffffff;
}
*{margin:0;padding:0;box-sizing:border-box}
html,body{width:1200px;height:4069px;overflow:hidden}
body{font-family:'Jost',sans-serif;color:var(--ink);background:var(--white);position:relative}
.abs{position:absolute}
a{color:inherit;text-decoration:none}

/* header + hero band */
.top-band{left:0;top:0;width:1200px;height:760px;background:linear-gradient(120deg,var(--blue-bright) 0%,#1a86df 45%,var(--blue-deep) 100%)}
.brand{left:200px;top:24px;display:flex;align-items:center;gap:10px;color:var(--white);font-weight:500;font-size:24px;letter-spacing:1px}
.brand-dot{width:26px;height:26px;border-radius:50%;background:var(--white)}
.main-nav{left:502px;top:36px;display:flex;gap:0;font-size:10.5px;color:var(--white);letter-spacing:.3px}
.main-nav a{position:absolute;white-space:nowrap}
.quote-btn{left:878px;top:21px;width:122px;height:45px;background:var(--white);border-radius:3px;color:var(--ink);font-size:10px;font-weight:600;display:flex;align-items:center;justify-content:center}

.hero{left:200px;top:87px;width:800px;height:374px;border-radius:4px;overflow:hidden;background:linear-gradient(180deg,#6fb6e4 0%,#a9d4ee 38%,#2f8fbf 55%,#27a6c4 78%,#c9b9a2 100%)}
.hero-shade{left:0;top:0;width:480px;height:374px;background:linear-gradient(90deg,rgba(40,28,18,.55),rgba(40,28,18,0))}
.hero-kicker{left:45px;top:54px;color:var(--white);font-size:9px;font-weight:500;display:flex;align-items:center;gap:10px}
.hero-kicker::before{content:"";width:34px;height:1px;background:var(--white)}
.hero-title{left:45px;top:74px;color:var(--white);font-size:46px;font-weight:500;line-height:50px;width:420px}
.hero-text{left:45px;top:185px;width:365px;color:var(--white);font-size:8.5px;line-height:14px}
.btn{background:var(--sky);color:var(--white);font-size:9px;font-weight:600;display:flex;align-items:center;justify-content:center;border-radius:2px;box-shadow:0 3px 8px rgba(0,60,120,.2)}
.hero-btn{left:45px;top:273px;width:107px;height:44px}
.play{left:609px;top:158px;width:58px;height:58px;border-radius:50%;background:rgba(255,255,255,.35);display:flex;align-items:center;justify-content:center}
.play span{width:42px;height:42px;border-radius:50%;background:var(--white);display:flex;align-items:center;justify-content:center}

.dots{display:flex;flex-direction:column;gap:22px;align-items:flex-end}
.dots i{display:block;height:2px;width:8px;background:var(--white)}
.dots i:first-child{width:18px}

.about-label{left:200px;top:532px;color:var(--white);font-size:11px;font-style:italic;font-weight:600;letter-spacing:4px}
.about-title{left:200px;top:556px;color:var(--white);font-size:16px;font-weight:600;letter-spacing:1.5px}
.about-text{left:406px;top:530px;width:594px;color:var(--white);font-size:8.6px;line-height:13.4px;font-weight:500}
.about-text p+p{margin-top:14px}
.wave{left:0;top:752px}

/* sections */
.section-title{left:0;width:1200px;text-align:center;font-size:23px;font-weight:500;letter-spacing:1.5px}
.service{width:160px;text-align:center;top:976px}
.service-icon{width:100px;height:100px;border-radius:50%;background:var(--sky-soft);margin:0 auto;display:flex;align-items:center;justify-content:center}
.service.active .service-icon{background:var(--sky)}
.service-name{margin-top:32px;font-size:15px;font-weight:600;letter-spacing:1.3px}
.service.active .service-name{color:var(--sky)}
.svc-lead{left:205px;top:1200px;width:313px;text-align:right;font-size:14px;font-weight:600;line-height:19.6px}
.svc-body{left:595px;top:1200px;width:406px;font-size:13.4px;font-weight:300;line-height:19.8px;color:#333}
.svc-btn{left:548px;top:1413px;width:107px;height:43px}

.projects-band{left:0;top:1550px;width:1000px;height:777px;background:linear-gradient(160deg,var(--blue-bright),var(--blue-deep))}
.projects-side{left:1000px;top:1550px;width:200px;height:777px;background:var(--pale)}
.project-photo{left:200px;top:1707px;width:902px;height:467px;background:linear-gradient(180deg,#c7d9e6 0%,#9fb8cc 45%,#5a89a8 70%,#7aa3b8 85%,#8c7a66 100%)}
.project-caption{left:200px;top:2095px;width:662px;height:79px;background:rgba(24,38,90,.82);color:var(--white);font-size:24px;font-weight:500;letter-spacing:2px;display:flex;align-items:center;padding-left:45px}

.quote-mark{left:0;top:2478px;width:1200px;text-align:center;color:var(--sky);font-size:96px;font-weight:700;line-height:96px}
.testimonial{left:300px;top:2577px;width:600px;text-align:center;font-size:14px;font-style:italic;font-weight:600;line-height:21.5px}
.author{left:0;top:2684px;width:1200px;text-align:center;font-size:11px;font-weight:600}
.author span{color:#8a94a6;font-weight:400}

.news-band{left:0;top:2787px;width:1200px;height:745px;background:var(--pale)}
.card{top:2965px;width:387px;text-align:center}
.card-photo{width:387px;height:235px;background:linear-gradient(180deg,#5fc4e8 0%,#2d9fd4 60%,#1c83be 100%)}
.card-title{margin-top:20px;font-size:16px;font-weight:500;line-height:24px;letter-spacing:.5px}
.card-date{margin-top:10px;font-size:16px;color:#555;letter-spacing:1px}
.card-text{margin:10px auto 0;width:370px;font-size:12.4px;font-weight:300;line-height:20px;color:#333}
.card .btn{width:109px;height:42px;margin:22px auto 0}

.subscribe{left:0;top:3532px;width:1200px;height:246px;background:var(--navy);overflow:hidden}
.sub-title{left:200px;top:82px;color:var(--white);font-size:28px;font-weight:500;line-height:43px}
.sub-field{left:586px;top:108px;width:414px;height:28px;border-bottom:1px solid rgba(255,255,255,.5);display:flex;align-items:flex-start;gap:10px;color:var(--white);font-size:9.5px}
.sub-btn{left:920px;top:111px;width:80px;height:25px;border:1px solid var(--white);border-radius:13px;color:var(--white);font-size:9px;display:flex;align-items:center;justify-content:center;gap:8px}

.footer-left{left:0;top:3778px;width:406px;height:291px;background:var(--white);border-right:1px solid #e5e7eb}
.footer-brand{left:200px;top:32px;display:flex;align-items:center;gap:8px;color:var(--blue-deep);font-size:20px;font-weight:500;letter-spacing:1px}
.footer-brand i{width:20px;height:20px;background:var(--blue-deep);border-radius:50%}
.footer-blurb{left:200px;top:105px;width:195px;font-size:8px;line-height:13px;color:#555}
.footer-mid{left:406px;top:3778px;width:412px;height:291px}
.footer-nav{top:53px;left:0;width:412px;display:flex;justify-content:center;gap:26px;font-size:10px}
.footer-rule{left:0;width:412px;height:1px;background:#e5e7eb}
.footer-col{top:144px;text-align:center;font-size:8px;line-height:12px;color:#555}
.footer-col b{display:block;color:var(--ink);font-weight:600;margin-bottom:6px}
.social{display:flex;gap:9px;justify-content:center;margin-top:4px}
.social i{width:10px;height:10px;border-radius:50%;background:var(--ink)}
.copyright{left:0;top:252px;width:412px;text-align:center;font-size:8.5px;color:#888}
.footer-join{left:818px;top:3778px;width:382px;height:291px;background:var(--sky);color:var(--white);text-align:center}
.join-title{margin-top:80px;font-size:30px;font-weight:300}
.join-text{margin-top:8px;font-size:16px;font-weight:300;line-height:21px}
.join-btn{margin:20px auto 0;width:108px;height:22px;border:1px solid var(--white);border-radius:12px;font-size:8.5px;display:flex;align-items:center;justify-content:center;gap:8px}
</style>
</head>
<body>

<div class="abs top-band"></div>

<header>
  <div class="abs brand"><span class="brand-dot"></span>MARLOW AQUATICS</div>
  <nav class="abs main-nav" style="left:0;top:36px">
    <a style="left:502px">HOME</a>
    <a style="left:560px">ABOUT US</a>
    <a style="left:638px">SERVICES</a>
    <a style="left:707px">BLOG</a>
    <a style="left:763px">CONTACT US</a>
  </nav>
  <a class="abs quote-btn">REQUEST A QUOTE</a>
</header>

<section class="abs hero" role="img" aria-label="Infinity pool on a terrace overlooking a tropical bay with palms and islands">
  <div class="abs hero-shade"></div>
  <div class="abs hero-kicker">YOUR DREAM SWIMMING POOL</div>
  <h1 class="abs hero-title">Build Your Dream Swimming Pool</h1>
  <p class="abs hero-text">Suspendisse consequat laoreet ultricies. Aenean ut tortor eros. Cras commodo nunc vitae ipsum auctor elementum. Duis congue quam mattis sodales condimentum. Proin porttitor, orci non pharetra bibendum, ante lectus sollicitudin metus, quis ultricies risus urna ac libero. Praesent at dictum sed quam pulvinar porta fringilla in felis. Morbi sed ut risus quam. Donec volutpat ut justo vitae commodo. Nam luctus tempor fermentum.</p>
  <a class="abs btn hero-btn">LEARN MORE</a>
  <div class="abs play"><span><svg width="14" height="14" viewBox="0 0 14 14"><path d="M3 1 L12 7 L3 13Z" fill="#1463c6"/></svg></span></div>
</section>

<div class="abs dots" style="left:1056px;top:237px"><i></i><i></i><i></i><i></i></div>

<section>
  <div class="abs about-label">ABOUT US</div>
  <h2 class="abs about-title">WHO WE ARE?</h2>
  <div class="abs about-text">
    <p>Lorem ipsum dolor sit amet, consectetur adipiscing elit. Sed faucibus elementum massa, vitae pellentesque justo molestie euismod. Ut facilisis at augue at laoreet. Duis diam enim, mattis ut venenatis quis, bibendum ac libero. Mauris sed vehicula orci, ac euismod massa. Nulla posuere, lorem id fringilla vulputate, dolor lectus volutpat odio, eu rutrum ante orci vitae purus. Cras consectetur erat at erat sagittis, eu pretium ante auctor. Maecenas pulvinar ligula ex, at vestibulum urna finibus eu. Phasellus hendrerit eros lacus, id sodales turpis egestas eget. Nunc commodo posuere nulla sed condimentum. Donec sed consequat massa. Aliquam vulputate est et turpis lobortis elementum. Curabitur posuere tincidunt ornare. Integer venenatis sem at elit laoreet, at eleifend mauris sodales.</p>
    <p>Fusce eget justo sit amet quam pharetra vehicula vel quis leo. Proin lobortis varius dui, eget commodo ex malesuada eget. In nec ultrices felis. Sed pharetra consequat gravida. Cras eu accumsan lacus, sit amet facilisis arcu. Nullam ut mauris sed ligula commodo imperdiet. Quisque vitae dolor tellus. Etiam at neque nec massa porttitor ullamcorper in porttitor orci. Ut lobortis dapibus venenatis. Duis ex lorem, bibendum sed velit ac, aliquam laoreet tellus.</p>
  </div>
</section>

<svg class="abs wave" width="1200" height="16" viewBox="0 0 1200 16">
  <defs><pattern id="scallop" width="12" height="16" patternUnits="userSpaceOnUse"><path d="M0 8 Q6 0 12 8 V16 H0Z" fill="#fff"/></pattern></defs>
  <rect width="1200" height="16" fill="url(#scallop)"/>
</svg>

<section>
  <h2 class="abs section-title" style="top:862px">OUR SERVICES</h2>

  <div class="abs service active" style="left:182px">
    <div class="service-icon"><svg width="56" height="56" viewBox="0 0 56 56" fill="none" stroke="#fff" stroke-width="2.2" stroke-linecap="round"><path d="M20 8v24M34 8v24M20 16h14M20 24h14"/><path d="M6 34q5-4 11 0t11 0 11 0 11 0M6 42q5-4 11 0t11 0 11 0 11 0M6 50q5-4 11 0t11 0 11 0 11 0"/></svg></div>
    <div class="service-name">NEW POOLS</div>
  </div>
  <div class="abs service" style="left:362px">
    <div class="service-icon"><svg width="56" height="56" viewBox="0 0 56 56" fill="none" stroke="#46b6e6" stroke-width="1.8" stroke-linecap="round"><circle cx="16" cy="28" r="9"/><circle cx="38" cy="22" r="11"/><path d="M16 37v12M38 33v16M6 49h44"/></svg></div>
    <div class="service-name">LANDSCAPING</div>
  </div>
  <div class="abs service" style="left:537px">
    <div class="service-icon"><svg width="56" height="56" viewBox="0 0 56 56" fill="none" stroke="#46b6e6" stroke-width="2" stroke-linecap="round" stroke-linejoin="round"><path d="M12 44l18-18M30 26a8 8 0 1 1 8 8M38 34l-4 4"/><path d="M44 44L22 22l-6-10-4 4 10 6"/></svg></div>
    <div class="service-name">REPAIR</div>
  </div>
  <div class="abs service" style="left:700px">
    <div class="service-icon"><svg width="56" height="56" viewBox="0 0 56 56" fill="none" stroke="#46b6e6" stroke-width="1.8" stroke-linecap="round"><path d="M8 28h40v8a8 8 0 0 1-8 8H16a8 8 0 0 1-8-8z"/><path d="M14 28V14a4 4 0 0 1 8 0M16 44l-2 5M40 44l2 5M16 34h24"/></svg></div>
    <div class="service-name">REMODEL</div>
  </div>
  <div class="abs service" style="left:863px">
    <div class="service-icon"><svg width="56" height="56" viewBox="0 0 56 56" fill="none" stroke="#46b6e6" stroke-width="1.8" stroke-linejoin="round"><path d="M10 20l18-9 18 9v18l-18 9-18-9z"/><path d="M10 20l18 9 18-9M28 29v18"/></svg></div>
    <div class="service-name">PRODUCTS</div>
  </div>

  <p class="abs svc-lead">Ut enim ad minim veniam, quis nostrud exercitation ullamco laboris nisi ut aliquip ex ea commodo consequat. Duis aute irure dolor in reprehendecat cupidatat non proidem. Sed ut perspiciatis unde omnis iste natus error sit voluptatem accusantium doloremque laudantium, totam rem periam, eaque ipsa quae ab illo inventore veritatis</p>
  <p class="abs svc-body">Lorem ipsum dolor sit amet, consectetur adipiscing elit. Integer tellus urna, tristique non erat a, fringilla dapibus mauris. Fusce eleifend ipsum vel dui tempus, eu convallis velit hendrerit. Donec efficitur rhoncus quam, eget ullamcorper justo. Aenean ipsum enim, condimentum sit amet risus vel, posuere tincidunt quam. Aenean a leo nec velit dapibus pellentesque. In non fringilla felis, non viverra tellus. Pellentesque habitant morbi tristique senectus et netus et malesuada fames ac turpis egestas.</p>
  <a class="abs btn svc-btn">LEARN MORE</a>
</section>

<section>
  <div class="abs projects-band"></div>
  <div class="abs projects-side"></div>
  <h2 class="abs section-title" style="top:1613px;color:#fff">OUR PROJECTS</h2>
  <div class="abs project-photo" role="img" aria-label="Indoor spa pool on a high floor with floor-to-ceiling windows over a city skyline"></div>
  <div class="abs project-caption">57TH FLOOR SPA AT THE DELMAR BRIGHTWATER</div>
  <div class="abs dots" style="left:78px;top:1902px"><i></i><i></i><i></i><i></i></div>
  <svg class="abs" style="left:1130px;top:1904px" width="30" height="68" viewBox="0 0 30 68" fill="none" stroke="#1b1f2a" stroke-width="1.4"><path d="M28 8H2M7 3L2 8l5 5"/><path d="M2 59h26M23 54l5 5-5 5"/></svg>
</section>

<section>
  <h2 class="abs section-title" style="top:2424px">WHAT PEOPLE SAY</h2>
  <div class="abs quote-mark">“</div>
  <p class="abs testimonial">Being able to swim in a luxury swimming pool at your own place is amazing! And I know for sure that the quality of service and technical experience of your company is the best. Thank you for everything!</p>
  <div class="abs author">DANIEL REYES, <span>WESTFIELD, PA</span></div>
  <svg class="abs" style="left:198px;top:2607px" width="28" height="12" viewBox="0 0 28 12" fill="none" stroke="#1b1f2a" stroke-width="1.4"><path d="M27 6H1M6 1L1 6l5 5"/></svg>
  <svg class="abs" style="left:975px;top:2607px" width="28" height="12" viewBox="0 0 28 12" fill="none" stroke="#1b1f2a" stroke-width="1.4"><path d="M1 6h26M22 1l5 5-5 5"/></svg>
</section>

<section>
  <div class="abs news-band"></div>
  <h2 class="abs section-title" style="top:2880px">LATEST NEWS</h2>
  <article class="abs card" style="left:199px">
    <div class="card-photo" role="img" aria-label="Two swimmers training with floats in an indoor pool"></div>
    <h3 class="card-title">Donec suscipit sem non nisi ultrices sagittis.<br>Etiam hendrerit lorem quis dolor</h3>
    <div class="card-date">April 19, 23</div>
    <p class="card-text">Lorem ipsum dolor sit amet, consectetur adipiscing elit. Integer tellus urna, tristique non erat a, fringilla dapibus mauris. Fusce eleifend ipsum vel dui tempus, eu convallis.</p>
    <a class="btn">LEARN MORE</a>
  </article>
  <article class="abs card" style="left:613px">
    <div class="card-photo" role="img" aria-label="Older swimmers doing aquatic therapy with kickboards"></div>
    <h3 class="card-title">Donec suscipit sem non nisi ultrices sagittis.<br>Etiam hendrerit lorem quis dolor</h3>
    <div class="card-date">April 19, 23</div>
    <p class="card-text">Lorem ipsum dolor sit amet, consectetur adipiscing elit. Integer tellus urna, tristique non erat a, fringilla dapibus mauris. Fusce eleifend ipsum vel dui tempus, eu convallis.</p>
    <a class="btn">LEARN MORE</a>
  </article>
</section>

<section class="abs subscribe">
  <h2 class="abs sub-title">Subscribe to our<br>mailing list</h2>
  <div class="abs sub-field"><svg width="18" height="13" viewBox="0 0 18 13" fill="none" stroke="#fff" stroke-width="1.2"><rect x=".6" y=".6" width="16.8" height="11.8" rx="1"/><path d="M1 1l8 6 8-6"/></svg>Email address</div>
  <a class="abs sub-btn">Submit <svg width="10" height="8" viewBox="0 0 10 8" fill="none" stroke="#fff" stroke-width="1.2"><path d="M0 4h9M6 1l3 3-3 3"/></svg></a>
  <svg class="abs" style="left:1050px;top:80px" width="140" height="120" viewBox="0 0 140 120" fill="none" stroke="rgba(255,255,255,.18)" stroke-width="3"><g transform="rotate(-28 70 60)"><rect x="15" y="25" width="110" height="72" rx="4"/><path d="M17 28l53 40 53-40"/></g></svg>
</section>

<footer>
  <div class="abs footer-left">
    <div class="abs footer-brand"><i></i>MARLOW AQUATICS</div>
    <p class="abs footer-blurb">Lorem ipsum dolor sit amet, consectetur adipiscing elit. Sed faucibus elementum massa, vitae pellentesque justo molestie euismod. Ut facilisis at augue at laoreet. Duis diam enim, mattis ut venenatis quis, bibendum ac libero. Mauris sed vehicula orci, ac euismod massa.</p>
  </div>
  <div class="abs footer-mid">
    <nav class="abs footer-nav"><a>HOME</a><a>ABOUT US</a><a>SERVICES</a><a>BLOG</a><a>CONTACT US</a></nav>
    <div class="abs footer-rule" style="top:112px"></div>
    <div class="abs footer-col" style="left:20px;width:120px"><b>Address</b>2210 Harbor Lane, Suite 300<br>Westfield, PA 19000</div>
    <div class="abs footer-col" style="left:150px;width:110px"><b>Follow us</b><div class="social"><i></i><i></i><i></i><i></i></div></div>
    <div class="abs footer-col" style="left:270px;width:130px"><b>Phone &amp; Email</b>(555) 014-2290<br>hello@marlowaquatics.com</div>
    <div class="abs footer-rule" style="top:226px"></div>
    <div class="abs copyright">Copyright © 2023 Marlow Aquatics. All Rights Reserved.</div>
  </div>
  <div class="abs footer-join">
    <div class="join-title">Join Today!</div>
    <p class="join-text">For more details about our<br>services and offers</p>
    <a class="join-btn">Inquire Today <svg width="10" height="8" viewBox="0 0 10 8" fill="none" stroke="#fff" stroke-width="1.2"><path d="M0 4h9M6 1l3 3-3 3"/></svg></a>
  </div>
</footer>

</body>
</html>
```